Tidewell Provisions

Distributor of seasonings and spices to the restaurant industry.

Restaurant

Tidewell Provis
Dean Holcroft
TK Wandsley Distributor
317-640-8917
dean@tidewellprovisionsco.com

No minimum order
Gluten & MSG free soup bases

```html
<!DOCTYPE html>
<html lang="en">
<head>
<meta charset="utf-8">
<title>Tidewell Provisions – Business Card</title>
<link rel="stylesheet" href="https://fonts.googleapis.com/css2?family=Open+Sans:wght@400;600&display=swap">
<style>
  :root {
    --backdrop: #e6e3e0;
    --card: #ffffff;
    --ink: #3a3433;
    --ink-soft: #4d4746;
    --accent: #ea7a45;
    --accent-warm: #f2a93b;
    --divider: #c9c6c4;
  }
  * { box-sizing: border-box; margin: 0; padding: 0; }
  html, body {
    width: 1200px;
    height: 900px;
    overflow: hidden;
    background: var(--backdrop);
    font-family: "Open Sans", Arial, sans-serif;
    color: var(--ink);
  }
  .canvas {
    width: 1200px;
    height: 900px;
    display: flex;
    align-items: center;
    justify-content: center;
    gap: 40px;
  }
  .card {
    position: relative;
    width: 540px;
    height: 309px;
    background: var(--card);
    box-shadow: 0 6px 18px rgba(0,0,0,0.18);
    overflow: hidden;
  }

  /* Brand name lockup */
  .brand {
    display: flex;
    align-items: center;
    gap: 10px;
  }
  .brand-dot {
    width: 16px;
    height: 16px;
    border-radius: 50%;
    background: var(--accent);
    flex-shrink: 0;
  }
  .brand-name {
    font-weight: 600;
    color: var(--ink);
    line-height: 1.1;
  }

  /* Front: contact side */
  .card-front .brand {
    position: absolute;
    left: 34px;
    top: 128px;
    width: 200px;
  }
  .card-front .brand-name { font-size: 24px; }
  .card-front .divider {
    position: absolute;
    left: 262px;
    top: 36px;
    width: 1px;
    height: 236px;
    background: linear-gradient(to bottom, transparent, var(--divider) 30%, var(--divider) 70%, transparent);
  }
  .contact {
    position: absolute;
    left: 292px;
    top: 74px;
  }
  .contact-name {
    font-size: 17px;
    font-weight: 600;
    color: var(--accent);
  }
  .contact-role {
    font-size: 12px;
    color: var(--ink-soft);
    margin-top: 2px;
  }
  .contact-list {
    list-style: none;
    margin-top: 22px;
  }
  .contact-item {
    display: flex;
    align-items: center;
    gap: 10px;
    font-size: 12.5px;
    color: var(--ink-soft);
    margin-bottom: 8px;
  }
  .contact-icon { width: 12px; height: 12px; flex-shrink: 0; }

  /* Back: brand side */
  .card-back .brand {
    position: absolute;
    left: 0;
    right: 0;
    top: 88px;
    justify-content: center;
  }
  .card-back .brand-name { font-size: 32px; }
  .tagline {
    position: absolute;
    left: 0;
    right: 0;
    top: 206px;
    text-align: center;
    font-size: 12px;
    font-weight: 600;
    line-height: 1.45;
    color: var(--ink);
  }
</style>
</head>
<body>
  <main class="canvas">
    <section class="card card-front" aria-label="Business card, contact side">
      <div class="brand">
        <span class="brand-dot"></span>
        <span class="brand-name">Tidewell Provisions</span>
      </div>
      <div class="divider"></div>
      <div class="contact">
        <p class="contact-name">Dean Holcroft</p>
        <p class="contact-role">TK Wandsley Distributor</p>
        <ul class="contact-list">
          <li class="contact-item">
            <svg class="contact-icon" viewBox="0 0 12 12" aria-hidden="true">
              <rect x="3" y="0.8" width="6" height="10.4" rx="1.2" fill="none" stroke="var(--accent)" stroke-width="1.2"/>
              <circle cx="6" cy="9.3" r="0.7" fill="var(--accent)"/>
            </svg>
            <span>317-640-8917</span>
          </li>
          <li class="contact-item">
            <svg class="contact-icon" viewBox="0 0 12 12" aria-hidden="true">
              <rect x="0.8" y="2.5" width="10.4" height="7" fill="var(--accent)"/>
              <path d="M0.8 2.5 L6 6.5 L11.2 2.5" fill="none" stroke="#fff" stroke-width="1"/>
            </svg>
            <span>dean@tidewellprovisionsco.com</span>
          </li>
        </ul>
      </div>
    </section>

    <section class="card card-back" aria-label="Business card, brand side">
      <div class="brand">
        <span class="brand-dot"></span>
        <span class="brand-name">Tidewell Provisions</span>
      </div>
      <p class="tagline">No Minimum Order<br>Gluten &amp; MSG Free Soup Bases</p>
    </section>
  </main>
</body>
</html>
```